Maple Hollow Bloom Panels Business card

Looking to have a business card design incorporating my logo for my flower wall business.

Industry/Entity Type

Wedding & event planning

Contact Information for Business Card

My business logo, my name - Lena Whitcombe (owner), my tagline - Let us be your something extra, phone # 401-726-3148, email address - maplehollowbloompanels@mailvane.net, my website - maplehollowbloompanels.net, Instagram handle- @maplehollowbloompanels, FB handle Handle - maplehollowbloompanels

Font styles to use
Other font styles liked:
• Sentaina is the font that is used in my logo

Requirements
Must have
• Would like a double sided business card

```html
<!DOCTYPE html>
<html lang="en">
<head>
<meta charset="utf-8">
<title>Maple Hollow Bloom Panels – Business Card</title>
<link href="https://fonts.googleapis.com/css2?family=Roboto:wght@300;400;500&display=swap" rel="stylesheet">
<style>
  :root {
    --page-bg: #f7f7f8;
    --card-white: #faf8fb;
    --card-pink: #f7dfe9;
    --ink: #1c1c1e;
    --ink-soft: #2b2b2e;
    --rose: #e19bc1;
    --rose-soft: #f1c9dd;
    --disc: #ffffff;
    --shadow: 0 4px 14px rgba(0,0,0,0.18);
  }
  * { box-sizing: border-box; margin: 0; padding: 0; }
  html, body {
    width: 800px; height: 1200px; overflow: hidden;
    background: var(--page-bg);
    font-family: "Roboto", Arial, sans-serif;
  }
  .canvas { position: relative; width: 800px; height: 1200px; }

  .card {
    position: absolute; left: 60px;
    width: 680px; height: 388px;
    overflow: hidden; box-shadow: var(--shadow);
  }
  .card--front { top: 182px; background: var(--card-white); }
  .card--back { top: 630px; background: var(--card-pink); }

  /* Front */
  .holder { position: absolute; left: 54px; top: 54px; }
  .holder__name {
    font-size: 45px; font-weight: 400; color: var(--ink);
    letter-spacing: -0.5px; line-height: 1;
  }
  .holder__role {
    font-size: 26px; font-weight: 400; color: var(--rose);
    line-height: 1; margin-top: 0;
  }
  .contact-list { position: absolute; left: 54px; top: 164px; list-style: none; }
  .contact-list li, .social {
    display: flex; align-items: center;
    font-size: 18.5px; font-weight: 300; color: var(--ink-soft);
    height: 31px;
  }
  .icon { width: 14px; height: 14px; margin-right: 13px; flex: none; fill: var(--rose); }
  .social-row { position: absolute; left: 54px; top: 328px; display: flex; }
  .social + .social { margin-left: 40px; }
  .social__mark {
    width: 14px; height: 14px; border-radius: 3px;
    background: var(--rose); margin-right: 13px; flex: none;
  }
  .floral-art {
    position: absolute; left: 400px; top: 0; width: 280px; height: 344px;
    background: radial-gradient(ellipse at 60% 50%, var(--rose-soft) 0%, rgba(241,201,221,0.45) 45%, rgba(250,248,251,0) 72%);
  }

  /* Back */
  .brand-disc {
    position: absolute; left: 209px; top: 42px;
    width: 262px; height: 262px; border-radius: 50%;
    background: var(--disc);
    display: flex; align-items: center; justify-content: center;
    text-align: center;
  }
  .brand-disc__name {
    font-size: 26px; font-weight: 400; color: var(--ink);
    line-height: 1.25; width: 190px;
  }
  .tagline {
    position: absolute; left: 0; right: 0; top: 322px;
    text-align: center;
    font-size: 21px; font-weight: 300; color: var(--ink-soft);
    letter-spacing: 3.2px;
  }
</style>
</head>
<body>
<main class="canvas">
  <section class="card card--front" aria-label="Business card front">
    <div class="floral-art" role="img" aria-label="Pink line-drawn flower illustration with gold dots"></div>
    <header class="holder">
      <h1 class="holder__name">Lena Whitcombe</h1>
      <p class="holder__role">Owner</p>
    </header>
    <ul class="contact-list">
      <li>
        <svg class="icon" viewBox="0 0 24 24" aria-hidden="true"><path d="M6.6 10.8c1.4 2.8 3.8 5.1 6.6 6.6l2.2-2.2c.3-.3.7-.4 1-.2 1.1.4 2.3.6 3.6.6.6 0 1 .4 1 1V20c0 .6-.4 1-1 1C10.6 21 3 13.4 3 4c0-.6.4-1 1-1h3.5c.6 0 1 .4 1 1 0 1.3.2 2.5.6 3.6.1.3 0 .7-.2 1z"/></svg>
        401-726-3148
      </li>
      <li>
        <svg class="icon" viewBox="0 0 24 24" aria-hidden="true"><path d="M2 5h20v14H2z M2 5l10 8 10-8" /></svg>
        maplehollowbloompanels@mailvane.net
      </li>
      <li>
        <svg class="icon" viewBox="0 0 24 24" aria-hidden="true"><circle cx="12" cy="12" r="10"/><path d="M2 12h20M12 2c3 3 3 17 0 20M12 2c-3 3-3 17 0 20" stroke="#faf8fb" stroke-width="1.6" fill="none"/></svg>
        maplehollowbloompanels.net
      </li>
    </ul>
    <div class="social-row">
      <p class="social"><span class="social__mark" aria-hidden="true"></span>@maplehollowbloompanels</p>
      <p class="social"><span class="social__mark" aria-hidden="true"></span>maplehollowbloompanels</p>
    </div>
  </section>

  <section class="card card--back" aria-label="Business card back">
    <div class="brand-disc">
      <p class="brand-disc__name">Maple Hollow Bloom Panels</p>
    </div>
    <p class="tagline">LET US BE YOUR SOMETHING EXTRA</p>
  </section>
</main>
</body>
</html>
```